Business Card for national trucking company

need a professional yet minimalistic business card

We are a long haul trucking company specializing in produce and frozen
goods. I'm just looking for a professional yet minimilistic business card.
I don't have any preferencs for the style, color or imagery. I would like
for the card to be double sided and have only the business logo on one
side. Other than that, I don't have any requirements.

Industry/Entity Type

Business

Contact Information for Business Card

Company: Voren Trucking
Name: Mark Pell
Phone: 800-555-0192
Email: blank@vorentrucking.example

Font styles to use
Serif

```html
<!DOCTYPE html>
<html lang="en">
<head>
<meta charset="utf-8">
<title>Voren Trucking — Business Card</title>
<link rel="stylesheet" href="https://fonts.googleapis.com/css2?family=Cinzel:wght@600&family=Open+Sans:wght@400&display=swap">
<style>
  :root {
    --backdrop: #3a3a3a;
    --card-white: #f7f7f7;
    --navy: #0c3566;
    --orange: #f26f10;
    --ink: #444444;
  }
  * { box-sizing: border-box; margin: 0; padding: 0; }
  html, body { width: 1200px; height: 750px; overflow: hidden; }
  body { background: var(--backdrop); position: relative; }

  .card { position: absolute; top: 228px; width: 461px; height: 263px; overflow: hidden; }
  .card--front { left: 124px; background: var(--card-white); }
  .card--back { left: 618px; background: var(--navy); }

  .wordmark {
    position: absolute; left: 0; right: 0;
    display: flex; align-items: center; justify-content: center; gap: 10px;
    font-family: "Cinzel", "Times New Roman", serif; font-weight: 600;
    font-size: 27px; letter-spacing: 0.5px; white-space: nowrap;
  }
  .wordmark__mark { width: 22px; height: 22px; flex: none; }
  .card--front .wordmark { top: 74px; color: var(--navy); }
  .card--front .wordmark__mark { background: var(--orange); }
  .card--back .wordmark { top: 113px; color: var(--orange); }
  .card--back .wordmark__mark { background: var(--orange); }

  .holder {
    position: absolute; left: 74px; top: 174px; width: 165px; text-align: right;
    font-family: "Cinzel", "Times New Roman", serif; font-weight: 600;
    font-size: 18px; color: var(--orange); white-space: nowrap;
  }

  .contacts { position: absolute; left: 249px; top: 160px; list-style: none; }
  .contacts li {
    display: flex; align-items: center; gap: 7px; height: 17.5px;
    font-family: "Open Sans", Arial, sans-serif; font-size: 11px; color: var(--ink);
  }
  .contacts svg { width: 11px; height: 11px; flex: none; fill: var(--orange); }

  .edge-tab { position: absolute; top: 150px; width: 9px; height: 76px; }
  .edge-tab--left { left: 0; }
  .edge-tab--right { right: 0; }
</style>
</head>
<body>

<section class="card card--front" aria-label="Business card front">
  <div class="wordmark"><span class="wordmark__mark"></span>Voren Trucking</div>

  <p class="holder">Mark Pell</p>

  <ul class="contacts">
    <li>
      <svg viewBox="0 0 12 12" aria-hidden="true"><path d="M2.4 0.6 L4.2 2.9 L3.2 4.2 C3.8 5.6 5.4 7.3 7.8 8.8 L9.1 7.8 L11.4 9.6 L10 11.6 C5.6 11 1 6.4 0.4 2 Z"/></svg>
      800-555-0192
    </li>
    <li>
      <svg viewBox="0 0 12 12" aria-hidden="true"><path d="M0.5 2.5 H11.5 V9.5 H0.5 Z M1.3 3.2 L6 6.6 L10.7 3.2" stroke="#f7f7f7" stroke-width="0.9"/></svg>
      blank@vorentrucking.example
    </li>
    <li>
      <svg viewBox="0 0 12 12" aria-hidden="true"><circle cx="6" cy="6" r="5.6"/><path d="M3 3.2 C4.5 3 5.2 4.4 4.4 5.4 C3.6 6.2 4.6 7.6 3.8 9 M7.6 2 C7 3.6 8.6 4.4 9.8 4.2 M7.2 10.6 C7.2 9 8.6 8 10 8.4" stroke="#f7f7f7" stroke-width="0.9" fill="none"/></svg>
      vorentrucking.example
    </li>
  </ul>

  <svg class="edge-tab edge-tab--left" viewBox="0 0 9 76" aria-hidden="true"><path d="M0 0 H9 V66 L0 76 Z" fill="var(--navy)"/></svg>
  <svg class="edge-tab edge-tab--right" viewBox="0 0 9 76" aria-hidden="true"><path d="M9 0 V76 L0 68 V8 Z" fill="var(--orange)"/></svg>
</section>

<section class="card card--back" aria-label="Business card back">
  <div class="wordmark"><span class="wordmark__mark"></span>Voren Trucking</div>
</section>

</body>
</html>
```